LPS AUDITION

I need a post card design (front only) with this on it:
Leap Pulse Stride (this is the main title to be in all caps)
Auditions
Date: Thursday June 30th
6:30-8:30 PM in person
Address: 4172 Kestrel BLVD, Oakland CA 94605
video submissions turn in by Sunday July 3rd, 2022 email:LeapPulseStride22@movenote.test
Teens and Adults welcomed

SO PLEASE COME UP WITH A DESIGN THATS COLORFUL AND INVITING THX!

```html
<!DOCTYPE html>
<html lang="en">
<head>
<meta charset="utf-8">
<title>Leap Pulse Stride – Audition Postcard</title>
<link rel="stylesheet" href="https://fonts.googleapis.com/css2?family=Poppins:wght@400;500;600;700;800;900&family=Oswald:wght@500;600&display=swap">
<style>
  :root {
    --page-bg: #f2f2f4;
    --card-dark: #0b0a1c;
    --card-navy: #16103f;
    --band: #24176a;
    --pink: #ff3d9a;
    --magenta: #d43fe8;
    --violet: #7a3cff;
    --blue: #3f5bff;
    --cyan: #1fe3f0;
    --white: #ffffff;
    --ink-soft: #e8e6f5;
  }
  * { box-sizing: border-box; margin: 0; padding: 0; }
  html, body {
    width: 687px; height: 1200px; overflow: hidden;
    background: var(--page-bg);
    font-family: "Poppins", sans-serif;
  }
  .postcard {
    position: absolute; left: 24px; top: 386px;
    width: 640px; height: 427px; overflow: hidden;
    background:
      radial-gradient(ellipse at 70% 40%, #2a1a8a 0%, transparent 60%),
      linear-gradient(180deg, var(--card-dark) 0%, var(--card-navy) 55%, var(--card-dark) 100%);
    box-shadow: 0 6px 18px rgba(0,0,0,.25);
  }
  .dancer-photo {
    position: absolute; right: 0; top: 0; width: 285px; height: 427px;
    background:
      radial-gradient(ellipse at 45% 40%, rgba(70,190,255,.55) 0%, transparent 45%),
      radial-gradient(ellipse at 60% 75%, rgba(140,60,255,.5) 0%, transparent 55%),
      linear-gradient(180deg, #261a8c 0%, #2c1f9e 55%, #150f45 100%);
  }
  .title {
    position: absolute; left: 44px; top: 34px;
    font-weight: 800; font-size: 66px; line-height: 62px; letter-spacing: -1px;
  }
  .title span { display: block; }
  .title .grad {
    background: linear-gradient(180deg, var(--blue) 0%, var(--magenta) 35%, var(--pink) 70%);
    -webkit-background-clip: text; background-clip: text; color: transparent;
    filter: drop-shadow(3px 2px 0 rgba(90,70,255,.85));
  }
  .title .solid {
    color: var(--white);
    text-shadow: -3px 1px 0 var(--blue);
  }
  .audition-box {
    position: absolute; left: 40px; top: 246px; width: 163px; height: 79px;
    border: 1px solid var(--cyan);
  }
  .audition-label {
    position: absolute; left: 8px; top: -11px; padding: 0 3px;
    background: var(--card-navy); color: var(--white);
    font-size: 15px; font-weight: 500; letter-spacing: .5px; line-height: 20px;
  }
  .audition-date {
    position: absolute; left: 10px; top: 19px;
    font-family: "Oswald", sans-serif; font-weight: 600; font-size: 18px; line-height: 20px;
    color: var(--white); letter-spacing: -.3px;
  }
  .audition-date .day { color: var(--pink); }
  .audition-date sup { font-size: 10px; vertical-align: top; line-height: 12px; }
  .audition-time {
    position: absolute; left: 10px; top: 41px;
    font-size: 15.5px; font-weight: 500; color: var(--white); line-height: 20px;
  }
  .audition-time .pm { color: var(--pink); }
  .in-person {
    position: absolute; left: 12px; top: 70px; width: 81px; height: 13px;
    background: var(--cyan); color: var(--card-navy);
    font-size: 9.5px; font-weight: 500; text-align: center; line-height: 13px;
  }
  .submission {
    position: absolute; left: 218px; top: 243px;
    font-size: 11.5px; line-height: 15px; color: var(--ink-soft);
  }
  .submission .accent { color: var(--cyan); font-weight: 700; }
  .submission .gap { margin-top: 5px; }
  .address-bar {
    position: absolute; left: 226px; top: 315px; width: 218px; height: 12px;
    background: var(--pink); color: var(--white);
    font-size: 8.3px; font-weight: 500; line-height: 12px; padding-left: 10px;
    white-space: nowrap;
  }
  .address-pin {
    position: absolute; left: 214px; top: 310px; z-index: 2;
  }
  .welcome-band {
    position: absolute; left: 0; top: 345px; width: 640px; height: 40px;
    background: linear-gradient(90deg, var(--band) 0%, rgba(36,23,106,.6) 70%, transparent 100%);
    border-top: 1px solid rgba(31,227,240,.6);
    border-bottom: 1px solid rgba(31,227,240,.35);
  }
  .welcome-text {
    position: absolute; left: 40px; top: 6px;
    font-size: 20px; font-weight: 500; letter-spacing: 1.2px; color: var(--white); line-height: 28px;
    white-space: nowrap;
  }
  .welcome-text .accent {
    color: var(--cyan); font-weight: 700;
    text-shadow: 0 0 6px rgba(31,227,240,.7);
  }
</style>
</head>
<body>
  <main class="postcard">
    <div class="dancer-photo" role="img" aria-label="Ballet dancer on pointe with flowing blue and mint fabric in front of neon diamond lights"></div>

    <h1 class="title">
      <span class="grad">LEAP</span>
      <span class="solid">PULSE</span>
      <span class="grad">STRIDE</span>
    </h1>

    <section class="audition-box">
      <div class="audition-label">AUDITIONS</div>
      <div class="audition-date"><span class="day">THURSDAY</span> JUNE 30<sup>TH</sup></div>
      <div class="audition-time">6:30 <span class="pm">PM</span>–8:30 <span class="pm">PM</span></div>
      <div class="in-person">IN PERSON</div>
    </section>

    <section class="submission">
      <p>Video submissions turn in by</p>
      <p class="accent">SUNDAY JULY 3RD</p>
      <p class="gap">2022 email:</p>
      <p class="accent">LeapPulseStride22@movenote.test</p>
    </section>

    <div class="address-bar">4172 Kestrel BLVD, Oakland CA 94605</div>
    <svg class="address-pin" width="14" height="17" viewBox="0 0 14 17" aria-hidden="true">
      <path d="M7 1a4.5 4.5 0 0 0-4.5 4.5C2.5 9 7 13 7 13s4.5-4 4.5-7.5A4.5 4.5 0 0 0 7 1z" fill="#16103f" stroke="#ff3d9a" stroke-width="1.6"/>
      <circle cx="7" cy="5.5" r="1.6" fill="#ff3d9a"/>
      <ellipse cx="7" cy="14.5" rx="5" ry="1.5" fill="none" stroke="#ff3d9a" stroke-width="1.2"/>
    </svg>

    <section class="welcome-band">
      <p class="welcome-text">TEENS AND ADULTS <span class="accent">WELCOMED</span></p>
    </section>
  </main>
</body>
</html>
```